Pet Spa Brochure

We are currently rebranding our Pet Resort & Spa. We have already completed our new website (www.tqlpawhaven.com), business cards and logo (attached). We are currently working on our brochures and decided to take a different route in finishing them.

We are looking for a spa/massage, floral, oriental, relaxing, feminine and elegant design for the brochure specific to our Pet Spa services. We want professional and elegant but also original and unique if possible.

We mainly have dog customers but we also have cat customers so a picture of at least one cat would be perfect. Our Pet Resort (not Spa, just Resort) brochure can be found at www.tqlpawhaven.com/rates and is the first two links listed. If things work well for our Pet Spa brochure we will be going back to redo the Pet Resort brochure as well.

I'm uploading a psd of the current brochure design so that you have access to the content. I can adjust the files later to make everything (or anything new) fit but please take the amount of text (present and future) into account when doing the design. I'm also uploading the psd of our current logo so it can be incorporated into the brochure as well.

The final design should communicate elegance, relaxation, pampering and happiness.
Updates

I'm attaching some of our pictures with pets in our pool, as well as some photos I saw on snapvaultimages that show dogs being pampered/rubbed/massaged. The links to the photos are below. I'll be uploading the others to the project attachment area.

Target Market(s)

Women between the ages of 25 and 55

Industry/Entity Type

Business

Requirements
Must have
• Animals, paw prints, our logo, floral, oriental hot springs/spa feel.
Should not have
• Cartoon animals or cartoon like clipart.

```html
<!DOCTYPE html>
<html lang="en">
<head>
<meta charset="utf-8">
<title>Pet Spa Brochure – Rates</title>
<link rel="stylesheet" href="https://fonts.googleapis.com/css2?family=Cormorant+SC:wght@500;600;700&display=swap">
<style>
  :root {
    --paper: #ffffff;
    --heading: #b5175f;
    --ink: #6a0d38;
    --leader: #9a6a80;
    --vine: #cfe6c4;
    --band-deep: #9c1247;
    --band-bright: #ff6a9f;
    --tree: #e84f8c;
  }
  * { margin: 0; padding: 0; box-sizing: border-box; }
  html, body { width: 1200px; height: 933px; overflow: hidden; background: var(--paper); }
  .spread {
    position: relative; width: 1200px; height: 933px; overflow: hidden;
    background: var(--paper);
    font-family: "Cormorant SC", "Times New Roman", serif;
    color: var(--ink);
  }
  .vine { position: absolute; border-radius: 50%; opacity: .55;
    background: radial-gradient(ellipse at center, var(--vine) 0%, rgba(207,230,196,0) 70%); }
  .vine--top-left { left: 120px; top: 0; width: 160px; height: 260px; }
  .vine--bottom-left { left: 0; top: 560px; width: 420px; height: 340px; }
  .vine--centre { left: 440px; top: 330px; width: 340px; height: 560px; }
  .vine--right { left: 900px; top: 500px; width: 300px; height: 400px; }
  .spa-tree { position: absolute; left: 963px; top: 797px; width: 124px; height: 118px;
    border-radius: 45% 55% 20% 20%;
    background: radial-gradient(ellipse at 50% 40%, var(--tree) 0%, #d23f7c 70%, rgba(210,63,124,.3) 100%); }
  .bands { position: absolute; left: 0; top: 0; width: 1200px; height: 933px; }
  .column { position: absolute; top: 22px; width: 352px; }
  .column--left { left: 29px; }
  .column--right { left: 425px; }
  .section-title, .rate, .tier {
    height: 21.7px; line-height: 21.7px; white-space: nowrap;
  }
  .section-title {
    margin-top: 10px; color: var(--heading); font-size: 20px; font-weight: 600; letter-spacing: .2px;
  }
  .section-title:first-child { margin-top: 0; }
  .section-title--spaced { margin-top: 25px; }
  .rate {
    margin-top: 10px; display: flex; align-items: baseline;
    font-size: 17.5px; font-weight: 700;
  }
  .rate__name { flex: none; }
  .rate__leader { flex: 1; border-bottom: 1px dotted var(--leader); margin: 0 2px; transform: translateY(-4px); }
  .rate__price { flex: none; }
  .tier { position: relative; font-size: 17px; font-weight: 600; }
  .tier span { position: absolute; top: 0; }
  .tier .c1 { left: 0; } .tier .c2 { left: 124px; } .tier .c3 { left: 187px; } .tier .c4 { left: 311px; }
  .tier .min { left: 141px; }
  .tier--wide .min { left: 142px; }
  .footnote { margin-top: 61px; font-size: 14.5px; font-weight: 500; font-family: "Cormorant SC", serif; text-transform: none; }
</style>
</head>
<body>
<main class="spread">
  <div class="vine vine--top-left" role="img" aria-label="Soft green floral vine decoration"></div>
  <div class="vine vine--bottom-left" role="img" aria-label="Soft green floral vine decoration"></div>
  <div class="vine vine--centre" role="img" aria-label="Soft green floral vine decoration"></div>
  <div class="vine vine--right" role="img" aria-label="Soft green floral vine decoration"></div>

  <svg class="bands" viewBox="0 0 1200 933" aria-hidden="true">
    <defs>
      <linearGradient id="bandLeft" x1="0" x2="1">
        <stop offset="0" stop-color="var(--band-deep)"/>
        <stop offset="1" stop-color="var(--band-bright)"/>
      </linearGradient>
      <linearGradient id="bandRight" x1="0" x2="1">
        <stop offset="0" stop-color="var(--band-bright)"/>
        <stop offset=".55" stop-color="#e04a86"/>
        <stop offset="1" stop-color="var(--band-deep)"/>
      </linearGradient>
    </defs>
    <path d="M0 903 Q170 880 348 933 L0 933Z" fill="url(#bandLeft)"/>
    <path d="M565 933 Q790 878 1010 886 Q1120 890 1200 912 L1200 933Z" fill="url(#bandRight)"/>
  </svg>

  <div class="spa-tree" role="img" aria-label="Pink blossom tree illustration"></div>

  <section class="column column--left">
    <h2 class="section-title">Feline Spa Services</h2>
    <p class="rate"><span class="rate__name">Bath</span><span class="rate__leader"></span><span class="rate__price">$25</span></p>
    <p class="rate"><span class="rate__name">Bath &amp; Nails</span><span class="rate__leader"></span><span class="rate__price">$30</span></p>
    <p class="rate"><span class="rate__name">Flea Bath</span><span class="rate__leader"></span><span class="rate__price">$30</span></p>
    <p class="rate"><span class="rate__name">Nails Only</span><span class="rate__leader"></span><span class="rate__price">$10</span></p>
    <p class="rate"><span class="rate__name">Brushout/Dematting</span><span class="rate__leader"></span><span class="rate__price">$40/hr + Bath</span></p>

    <h2 class="section-title section-title--spaced">Canine Spa Services</h2>
    <p class="rate"><span class="rate__name">Bath</span><span class="rate__leader"></span><span class="rate__price">See Below</span></p>
    <p class="tier"><span class="c1">Under 20lbs</span><span class="c2">$20</span><span class="c3">81 - 110lbs</span><span class="c4">$35</span></p>
    <p class="tier"><span class="c1">21 - 50lbs</span><span class="c2">$25</span><span class="c3">111lbs &amp; Over</span><span class="c4">$40</span></p>
    <p class="tier"><span class="c1">51 - 80lbs</span><span class="c2">$30</span></p>
    <p class="rate"><span class="rate__name">Bath &amp; Nails</span><span class="rate__leader"></span><span class="rate__price">See Below</span></p>
    <p class="tier"><span class="c1">Under 20lbs</span><span class="c2">$25</span><span class="c3">81 - 110lbs</span><span class="c4">$40</span></p>
    <p class="tier"><span class="c1">21 - 50lbs</span><span class="c2">$30</span><span class="c3">111lbs &amp; Over</span><span class="c4">$45</span></p>
    <p class="tier"><span class="c1">51 - 80lbs</span><span class="c2">$35</span></p>
    <p class="rate"><span class="rate__name">Nails Only</span><span class="rate__leader"></span><span class="rate__price">$10</span></p>
    <p class="rate"><span class="rate__name">Brushout/Dematting</span><span class="rate__leader"></span><span class="rate__price">$40/hr + Bath</span></p>
    <p class="rate"><span class="rate__name">Professional Grooming*</span><span class="rate__leader"></span><span class="rate__price">See Below</span></p>
    <p class="tier"><span class="c1">Under 20lbs</span><span class="min">At Least $40</span></p>
    <p class="tier"><span class="c1">21 - 50lbs</span><span class="min">At Least $50</span></p>
    <p class="tier"><span class="c1">51 - 80lbs</span><span class="min">At Least $60</span></p>
    <p class="tier"><span class="c1">81 - 110lbs</span><span class="min">At Least $70</span></p>
    <p class="tier"><span class="c1">111lbs &amp; Over</span><span class="min">At Least $80</span></p>
    <p class="rate"><span class="rate__name">Shedless Program*</span><span class="rate__leader"></span><span class="rate__price">$60 to $115</span></p>
    <p class="rate"><span class="rate__name">Flea Bath</span><span class="rate__leader"></span><span class="rate__price">$3 to $10 + Bath</span></p>
    <p class="rate"><span class="rate__name">Special Bath</span><span class="rate__leader"></span><span class="rate__price">$3 to $10 + Bath</span></p>
    <p class="rate"><span class="rate__name">Long Coats</span><span class="rate__leader"></span><span class="rate__price">Extra Charge</span></p>

    <p class="footnote">*Includes the price of a Bath in the rate.</p>
  </section>

  <section class="column column--right">
    <h2 class="section-title">Canine Spa Extras</h2>
    <p class="rate"><span class="rate__name">Anal Glands</span><span class="rate__leader"></span><span class="rate__price">$??</span></p>
    <p class="rate"><span class="rate__name">Scent of the Month</span><span class="rate__leader"></span><span class="rate__price">$5 + Bath</span></p>
    <p class="rate"><span class="rate__name">Bows/Bandannas</span><span class="rate__leader"></span><span class="rate__price">$??</span></p>
    <p class="rate"><span class="rate__name">Creative Grooming</span><span class="rate__leader"></span><span class="rate__price">$??</span></p>
    <p class="rate"><span class="rate__name">Whitening Treatment</span><span class="rate__leader"></span><span class="rate__price">$??</span></p>
    <p class="rate"><span class="rate__name">Teeth Brushing</span><span class="rate__leader"></span><span class="rate__price">$??</span></p>
    <p class="rate"><span class="rate__name">Temporary Airbrush Tattoos</span><span class="rate__leader"></span><span class="rate__price">See Below</span></p>
    <p class="tier tier--wide"><span class="c1">Under 20lbs</span><span class="min">At Least $40</span></p>
    <p class="tier tier--wide"><span class="c1">21 - 50lbs</span><span class="min">At Least $50</span></p>
    <p class="tier tier--wide"><span class="c1">51 - 80lbs</span><span class="min">At Least $60</span></p>
    <p class="tier tier--wide"><span class="c1">81 - 110lbs</span><span class="min">At Least $70</span></p>
    <p class="tier tier--wide"><span class="c1">111lbs &amp; Over</span><span class="min">At Least $80</span></p>
    <p class="rate"><span class="rate__name">Nail Polish</span><span class="rate__leader"></span><span class="rate__price">$60 to $115</span></p>
    <p class="rate"><span class="rate__name">Hot Towel Massage</span><span class="rate__leader"></span><span class="rate__price">$10</span></p>
    <p class="rate"><span class="rate__name">Hot Spring Session</span><span class="rate__leader"></span><span class="rate__price">$20</span></p>
    <p class="rate"><span class="rate__name">Hot Spring &amp; Towel Massage</span><span class="rate__leader"></span><span class="rate__price">$25</span></p>
    <p class="rate"><span class="rate__name">Playtime</span><span class="rate__leader"></span><span class="rate__price">$7</span></p>
    <p class="rate"><span class="rate__name">Downtime</span><span class="rate__leader"></span><span class="rate__price">$10</span></p>
  </section>
</main>
</body>
</html>
```